Flooring & Interior Design showroom

Just bought this business- Maple Terrace Flooring & Interiors. Love our logo (we are on Maple Terrace )and colors
Forest green, gold and black
Love that the back lists everything we do. We no longer have stonavelle but need to add in LVP/ SPC and need to take out tirelli shadehouse logo at the bottom and use the zumo logo instead (maybe? open to suggestions)

Not in love with our cards- I want a higher end look
I hate the gradient poop color we have now.
Would love if they were all black - maybe or ??
or had a foil or embossing?

```html
<!DOCTYPE html>
<html lang="en">
<head>
<meta charset="utf-8">
<title>Maple Terrace Flooring &amp; Interiors – Business Card</title>
<link rel="stylesheet" href="https://fonts.googleapis.com/css2?family=Gilda+Display&display=swap">
<style>
  :root {
    --page: #f4f1ec;
    --card: #0e1e15;
    --card-edge: #0a1710;
    --gold: #e9df8f;
    --ivory: #ebe6d6;
    --white: #ffffff;
    --badge: #d9d6cc;
  }
  * { box-sizing: border-box; margin: 0; padding: 0; }
  html, body {
    width: 800px; height: 1200px; overflow: hidden;
    background: var(--page);
    font-family: "Gilda Display", Georgia, serif;
  }
  .canvas { position: relative; width: 800px; height: 1200px; }
  .card {
    position: absolute;
    width: 727px; height: 430px;
    background: linear-gradient(160deg, var(--card) 0%, var(--card-edge) 100%);
    transform: scale(.935);
    transform-origin: top left;
    color: var(--ivory);
    overflow: hidden;
  }
  .card--front { left: 40px; top: 150px; }
  .card--back { left: 80px; top: 620px; }
  .card p, .card span { position: absolute; white-space: nowrap; }

  .brand-name {
    position: absolute; color: var(--gold);
    font-size: 27px; line-height: 1.05; letter-spacing: .5px;
  }
  .brand-name small { display: block; font-size: 13.5px; letter-spacing: 1.2px; margin-top: 4px; }

  .rule { position: absolute; left: 0; right: 0; background: var(--gold); }

  /* front */
  .holder-name { left: 62px; top: 100px; font-size: 31px; color: var(--gold); }
  .holder-title { left: 62px; top: 154px; font-size: 15px; color: var(--gold); }
  .info { font-size: 15px; }
  .info b { font-weight: normal; display: inline-block; width: 52px; }

  /* back */
  .tagline { right: 57px; top: 50px; font-size: 16px; }
  .back-phone { right: 57px; top: 78px; font-size: 22px; color: var(--gold); }
  .back-web { right: 57px; top: 110px; font-size: 14.5px; color: var(--gold); }
  .services {
    position: absolute; left: 55px; top: 205px;
    display: grid; grid-template-columns: 153px 154px 160px;
    row-gap: 8.5px; list-style: none; font-size: 13px;
  }
  .services li { display: flex; align-items: center; gap: 8px; line-height: 19px; }
  .services li::before {
    content: ""; width: 8px; height: 8px; border-radius: 50%;
    border: 1.5px solid var(--gold);
  }
  .partner-badge {
    position: absolute; left: 543px; top: 275px; width: 127px; height: 28px;
    border-radius: 3px; background: var(--badge);
  }
  .partner-name {
    left: 560px; top: 318px; font-size: 30px; color: var(--white);
  }
</style>
</head>
<body>
<main class="canvas">

  <section class="card card--front" aria-label="Business card front">
    <div class="brand-name" style="left:470px; top:82px;">Maple Terrace<small>FLOORING &amp; INTERIORS</small></div>
    <div class="rule" style="left:62px; top:146px; height:1px;"></div>

    <p class="holder-name">Dana Whitlock</p>
    <p class="holder-title">Owner/ Designer</p>

    <p class="info" style="left:62px; top:216px;">28 Maple Terrace,</p>
    <p class="info" style="left:62px; top:243px;">Carmel Ridge CA</p>
    <p class="info" style="left:62px; top:270px;">93900</p>
    <p class="info" style="left:62px; top:334px;">www.mapleterraceflooring.com</p>

    <p class="info" style="left:436px; top:216px;"><b>Store</b>555.214.0188</p>
    <p class="info" style="left:436px; top:243px;"><b>Fax</b>555.214.0190</p>
    <p class="info" style="left:436px; top:270px;"><b>Cell</b>555-309-4471</p>
    <p class="info" style="left:436px; top:302px;">dana@mapleterraceflooring.com</p>
    <p class="info" style="left:436px; top:334px;"><b>CA Lic</b>#401276</p>
  </section>

  <section class="card card--back" aria-label="Business card back">
    <div class="brand-name" style="left:90px; top:82px;">Maple Terrace<small>FLOORING &amp; INTERIORS</small></div>

    <p class="tagline">Home Town Service Since 1979</p>
    <p class="back-phone">555.214.0188</p>
    <p class="back-web">www.mapleterraceflooring.com</p>
    <div class="rule" style="top:144px; height:3px;"></div>

    <ul class="services">
      <li>Area Rugs</li><li>Sheers</li><li>Fabric</li>
      <li>Blinds</li><li>Valances</li><li>Motorized Shades</li>
      <li>Carpet</li><li>Vinyl</li><li>Pillows</li>
      <li>Cork</li><li>Bed Spreads</li><li>Shutters</li>
      <li>Hardwood</li><li>Draperies</li><li>Upholstery</li>
      <li>Laminate</li><li>LVP / SPC</li><li>Verticals</li>
    </ul>

    <div class="partner-badge" role="img" aria-label="Window fashions partner badge"></div>
    <span class="partner-name">zumo</span>
  </section>

</main>
</body>
</html>
```